South Carolina Bridal and Formal Wear Store

We want The Gown Parlor of Ashcombe website to feel luxurious, elegant, welcoming, and approachable—without feeling overpriced or intimidating. The site should immediately show that we are a full-service bridal and formal wear destination, offering bridal gowns, prom, mothers’ dresses, tuxedos and suits, accessories, and more. We want beautiful, high-end imagery and a clean, modern design while still reflecting the warm, personal experience customers receive when they walk into our boutique. Most importantly, the website should be easy to shop and navigate, allowing customers to browse our collections, see what we offer, understand price ranges, book appointments, and feel excited and comfortable choosing The Gown Parlor of Ashcombe for all of their special-event needs.

Target Market(s)

Women ages 18-50. Brides, engaged women, mothers of the occasion

Industry/Entity Type

Bridal and Formal Wear

Coding

Coded - Design and coding required

Number of Pages Required

5+ page

Font styles to use
Sans Serif

Colors

Designer to choose colors to be used in the design.

Requirements
Must have
• Appointment area, about us staff area, what we offer and designers our logo
Nice to have
• Modern Southern Luxury: Clean, elegant, and upscale with soft neutral tones, beautiful bridal photography, and a warm Lowcountry feel.
Should not have
• pricing

```html
<!DOCTYPE html>
<html lang="en">
<head>
<meta charset="utf-8">
<title>The Gown Parlor of Ashcombe</title>
<link rel="stylesheet" href="https://fonts.googleapis.com/css2?family=Cormorant+Garamond:ital,wght@0,400;0,500;1,400&family=Karla:wght@400;500&display=swap">
<style>
:root{
  --ink:#1c1a18;
  --black:#000;
  --white:#fff;
  --muted:#6e6a66;
  --soft:#a9a39c;
  --line:#d9d4cf;
  --gold:#b89a6a;
  --serif:'Cormorant Garamond', Georgia, serif;
  --sans:'Karla', Helvetica, Arial, sans-serif;
}
*{margin:0;padding:0;box-sizing:border-box}
html,body{width:1200px;height:3583px;overflow:hidden}
body{position:relative;font-family:var(--sans);color:var(--ink);background:var(--white)}
.abs{position:absolute}
.eyebrow{font-family:var(--sans);font-size:8.5px;letter-spacing:3px;text-transform:uppercase}
.btn{position:absolute;display:flex;align-items:center;justify-content:center;font-size:8.5px;letter-spacing:2.6px;text-transform:uppercase;border:1px solid currentColor}
.photo{position:absolute}

/* hero */
.hero{position:absolute;left:0;top:0;width:1200px;height:684px;background:linear-gradient(90deg,#191a17 0%,#2c2f28 35%,#5d6660 60%,#8c98a3 80%,#6a6d66 100%);color:var(--white)}
.hero .shade{position:absolute;inset:0;background:linear-gradient(90deg,rgba(0,0,0,.55),rgba(0,0,0,.1) 70%)}
.brand{position:absolute;font-family:var(--serif);font-size:16px;line-height:1.05;color:var(--white);letter-spacing:.3px}
.brand small{display:block;font-family:var(--sans);font-size:6px;letter-spacing:2.2px;text-transform:uppercase;margin-top:3px}
.nav{position:absolute;left:438px;top:53px;display:flex;gap:24px;font-size:8.5px;letter-spacing:2.2px;text-transform:uppercase}
.hero h1{position:absolute;left:97px;top:222px;font-family:var(--serif);font-weight:400;font-size:57px;line-height:63px}
.hero h1 em{font-style:italic}
.hero p{position:absolute;left:97px;top:440px;width:480px;font-size:12.5px;line-height:21px}

/* offer */
.offer h2,.designers h2,.cta h2,.experience h2{font-family:var(--serif);font-weight:400}
.offer h2{position:absolute;left:100px;top:813px;font-size:40px;line-height:50px;color:var(--ink)}
.offer .lede{position:absolute;left:566px;top:841px;width:520px;font-size:12px;line-height:21.5px;color:var(--muted)}
.card{position:absolute;top:958px;width:230px}
.card .photo{position:relative;width:230px;height:306px}
.card h3{font-family:var(--serif);font-weight:400;font-size:18.5px;margin-top:20px;color:#3a3733}
.card p{font-size:10.5px;line-height:19px;color:var(--muted);margin-top:6px;width:200px}

/* experience */
.experience{position:absolute;left:0;top:1523px;width:1200px;height:778px;background:var(--black);color:var(--white)}
.experience h2{position:absolute;left:623px;top:165px;font-size:40px;line-height:50px}
.experience .body{position:absolute;left:623px;top:292px;width:480px;font-size:12px;line-height:21.5px;color:#d8d4cf}
.points{position:absolute;left:623px;top:402px;width:478px;list-style:none}
.points li{height:44px;display:flex;align-items:center;font-size:10.5px;color:#d8d4cf;border-bottom:1px solid #2c2a28;padding-left:17px;position:relative}
.points li::before{content:"";position:absolute;left:2px;top:20px;width:4px;height:4px;border-radius:50%;background:var(--white)}

/* designers */
.designers h2{position:absolute;left:0;top:2425px;width:1200px;text-align:center;font-size:40px;line-height:50px;color:#2a2724}
.designers p{position:absolute;left:0;top:2550px;width:1200px;text-align:center;font-size:12px;line-height:21.5px;color:var(--muted)}

/* cta */
.cta{position:absolute;left:65px;top:2748px;width:1070px;height:364px;background:linear-gradient(100deg,#5a5a50,#8a8478 35%,#6a6a72 55%,#4e5a50 80%,#5c5448);color:var(--white);text-align:center}
.cta .shade{position:absolute;inset:0;background:rgba(0,0,0,.35)}
.cta h2{position:absolute;left:0;width:100%;top:95px;font-size:40px}
.cta p{position:absolute;left:260px;width:550px;top:161px;font-size:12px;line-height:19.5px}

/* footer */
.footer{position:absolute;left:0;top:3204px;width:1200px;height:379px;background:var(--black);color:var(--white)}
.footer .brand{font-size:24px}
.footer .brand small{font-size:8px}
.tagline{position:absolute;left:106px;top:180px;width:330px;font-family:var(--serif);font-size:16.5px;line-height:27px;color:#dcd8d3}
.fcol{position:absolute;font-size:10.5px;line-height:23px;color:#dcd8d3}
.fcol .eyebrow{color:#7c7670;margin-bottom:10px}
.hours{display:flex;justify-content:space-between;width:221px}
.legal{position:absolute;top:325px;font-size:8px;letter-spacing:2.4px;text-transform:uppercase;color:#8a847e}
</style>
</head>
<body>

<header class="hero">
  <div class="photo shade" role="img" aria-label="Wedding party of groomsmen in grey suits and bridesmaids in dusty blue gowns under moss-draped oaks"></div>
  <div class="brand" style="left:97px;top:44px">The Gown Parlor<small>of Ashcombe</small></div>
  <nav class="nav"><span>What we offer</span><span>Designers</span><span>Appointments</span><span>About us</span><span>FAQ</span><span>Visit</span></nav>
  <div class="btn" style="left:932px;top:43px;width:171px;height:33px;color:var(--white)">Request appointment</div>
  <div class="eyebrow abs" style="left:97px;top:188px">Ashcombe, South Carolina</div>
  <h1>Where the<br>Lowcountry<br><em>says yes.</em></h1>
  <p>From the first gown you slip into to the tuxedo he wears down the aisle, we are a full-service bridal and formal wear destination warm, personal, and unhurried.</p>
  <div class="btn" style="left:97px;top:537px;width:210px;height:39px;background:var(--white);color:var(--ink);border-color:var(--white)">Request an appointment</div>
  <div class="btn" style="left:321px;top:537px;width:205px;height:39px;color:var(--white)">Explore what we offer</div>
</header>

<section class="offer">
  <div class="eyebrow abs" style="left:100px;top:782px;color:var(--soft)">What we offer</div>
  <h2>One boutique for every<br>dress in the story</h2>
  <p class="lede">Bridal, bridesmaids, mothers of the occasion, tuxedos and suits, prom, formal wear, accessories, on-site steaming and wedding gown preservation all under one roof, with a consultant who knows your name.</p>
  <div class="card" style="left:100px"><div class="photo" role="img" aria-label="Bride in lace ball gown with groom in black tuxedo on a lawn" style="background:linear-gradient(180deg,#8fa27a,#c9cfc2 55%,#e8e6e0)"></div><h3>Bridal Gowns</h3><p>Curated designer gowns for every silhouette and story.</p></div>
  <div class="card" style="left:357px"><div class="photo" role="img" aria-label="Bride laughing with bridesmaids in floral blue dresses" style="background:linear-gradient(180deg,#6f8a5a,#c8b9a6 50%,#9fb0c6)"></div><h3>Bridesmaids</h3><p>Coordinated color palettes your whole party will love.</p></div>
  <div class="card" style="left:613px"><div class="photo" role="img" aria-label="Couple beside a vintage white car" style="background:linear-gradient(180deg,#6c7a62,#a9aaa4 50%,#4a4a48)"></div><h3>Mother of the Occasion</h3><p>Elegant, comfortable looks for the women who raised you.</p></div>
  <div class="card" style="left:870px"><div class="photo" role="img" aria-label="Bride and groom in blue suit celebrating under a petal toss" style="background:linear-gradient(180deg,#8d8a86,#c9bdb8 50%,#3f5588)"></div><h3>Tuxedos &amp; Suits</h3><p>Rental or purchase, with measurements taken in-store.</p></div>
  <div class="btn" style="left:512px;top:1393px;width:176px;height:37px;color:var(--ink)">See all services</div>
</section>

<section class="experience">
  <div class="photo" role="img" aria-label="Consultant showing a white gown to a bride among racks of dresses" style="left:100px;top:91px;width:477px;height:596px;background:linear-gradient(180deg,#e9e7e3,#cfc9c1 55%,#8a6a45)"></div>
  <div class="eyebrow abs" style="left:623px;top:136px;color:var(--gold)">The experience</div>
  <h2>Attention that never feels<br>rushed</h2>
  <p class="body">We cater to one bridal party at a time so you have our undivided attention. Your consultant will learn about your wedding day, your must-haves, and guide you through silhouettes and details until something feels unmistakably like you.</p>
  <ul class="points">
    <li>Samples from size 8–28, with orders available from 0–32</li>
    <li>Up to four guests or reserve the entire boutique for a VIP visit</li>
    <li>Tuxedos for rent or purchase, with direct shipping available</li>
    <li>Authorized retailer for the Heirloom Gown Care Society</li>
  </ul>
  <div class="btn" style="left:623px;top:606px;width:210px;height:40px;color:var(--gold)">View appointment types</div>
</section>

<section class="designers">
  <div class="eyebrow abs" style="left:0;top:2396px;width:1200px;text-align:center;color:var(--soft)">Our designers</div>
  <h2>Jolene Avery · Marisette · Talia Oren<br>· Evermore Bridal</h2>
  <p>Plus Wren &amp; Vale Collection, Harlow Finch, Ninth Hour, Belle Maison Maids, NVRA,<br>Castellane, June's Formal Wear and Harwick Formal Wear.</p>
  <div class="btn" style="left:530px;top:2627px;width:139px;height:29px;color:var(--ink)">Meet the labels</div>
</section>

<section class="cta" role="img" aria-label="Newlyweds walking through a crowd of guests tossing rose petals">
  <div class="shade"></div>
  <h2>Let's find the one, together</h2>
  <p>Walk-ins are always welcome requesting an appointment simply guarantees a consultant devoted to you.</p>
  <div class="btn" style="left:429px;top:232px;width:211px;height:39px;background:var(--white);color:var(--ink);border-color:var(--white)">Request an appointment</div>
</section>

<footer class="footer">
  <div class="brand" style="left:106px;top:92px">The Gown Parlor<small>of Ashcombe · Bridal · Formal wear</small></div>
  <p class="tagline">A full-service bridal and formal wear destination in the heart of the Lowcountry where every celebration begins.</p>
  <div class="fcol" style="left:540px;top:93px;width:230px">
    <div class="eyebrow">Visit us</div>
    220 Magnolia Row, Suite 4<br>Ashcombe, SC 29955<br>
    <div style="margin-top:10px">843-555-0142<br>appointments@gownparlorashcombe.com</div>
  </div>
  <div class="fcol" style="left:873px;top:93px;width:221px">
    <div class="eyebrow">Boutique hours</div>
    <div class="hours"><span>Wednesday – Saturday</span><span>10am – 6pm</span></div>
    <div class="hours"><span>Sunday – Tuesday</span><span>Closed</span></div>
    <div style="font-size:9px;line-height:15px;color:#7c7670;margin-top:8px">VIP bridal experiences available on Sundays by request.</div>
  </div>
  <div class="legal" style="left:100px">© 2026 The Gown Parlor of Ashcombe</div>
  <div class="legal" style="left:858px;display:flex;gap:24px"><span>Appointments</span><span>What we offer</span><span>FAQ</span></div>
</footer>

</body>
</html>
```